Silverpine Orbit Works Flyer

We need a one page promotional piece that explains what our company does, and the benefits it provides in a simple, elegant, easy to understand way. I would like to print it on glossy heavyweight paper to give a feel of high quality and legitimacy. I will include the logo, the tag line, and the main benefits that the company offers.

Tag line concept, may not need these exact words. "Lend us 5 minutes each morning, and we will guide you toward a Silverpine Orbit Works."

Key points...(exact wording not required if you think of a better way to say it)

Software easy enough for my grandpa to use.
Lets you use snail mail, email, texting, and social media to quickly market to your customers at very low cost.
Web based which allows you to launch media campaigns from your desktop, or smartphone in moments.
Quick 3 - 5 minute training videos which give you hard hitting, quick action tips that will help you make your business better today.
Live coaching calls to help motivate you to improve your business.
No contracts, or start up fees. One low price of $299 per month.

Restaurant owners

Restaurant

```html
<!DOCTYPE html>
<html lang="en">
<head>
<meta charset="utf-8">
<title>Silverpine Orbit Works Flyer</title>
<link href="https://fonts.googleapis.com/css2?family=PT+Sans+Narrow:wght@400;700&family=Roboto:wght@700&family=Roboto+Condensed:wght@700&display=swap" rel="stylesheet">
<style>
  :root {
    --flyer-bg: #393939;
    --badge-white: #ffffff;
    --brand-grey: #5a5a5a;
    --brand-dot: #a7a7a7;
    --headline-green: #7dc242;
    --text-white: #ffffff;
    --row-blue: #1b75bb;
    --row-red: #e8413a;
    --row-magenta: #e2237a;
    --row-green: #5aa246;
    --row-orange: #f58220;
    --tab-light: #d9d3c3;
    --tab-dark: #a79f8c;
    --tab-number: #f4f1ea;
  }
  * { box-sizing: border-box; margin: 0; padding: 0; }
  html, body { width: 922px; height: 1200px; overflow: hidden; }
  body { background: var(--flyer-bg); position: relative; font-family: "PT Sans Narrow", sans-serif; }

  .brand-badge { position: absolute; left: 159px; top: 0; width: 604px; height: 478px; }
  .brand-badge svg { display: block; }
  .brand-name {
    position: absolute; left: 0; right: 0; top: 296px;
    text-align: center; color: var(--brand-grey);
    font-family: "Roboto Condensed", sans-serif; font-weight: 700; font-size: 46px;
  }

  .tagline {
    position: absolute; left: 0; right: 0; top: 500px;
    text-align: center; color: var(--headline-green);
    font-family: "PT Sans Narrow", sans-serif; font-weight: 700;
    font-size: 54px; line-height: 74px;
  }

  .benefits-title {
    position: absolute; left: 0; right: 0; top: 758px;
    text-align: center; color: var(--text-white);
    font-family: "Roboto", sans-serif; font-weight: 700; font-size: 27px;
  }

  .benefit-list { list-style: none; position: absolute; left: 52px; top: 812px; width: 814px; }
  .benefit {
    position: relative; display: flex; align-items: center;
    margin-bottom: 8px; color: var(--text-white);
  }
  .benefit-number {
    flex: 0 0 72px; align-self: stretch;
    display: flex; align-items: center; justify-content: center;
    background: linear-gradient(90deg, var(--tab-light), var(--tab-dark));
    color: var(--tab-number);
    font-family: "PT Sans Narrow", sans-serif; font-weight: 700; font-size: 60px; line-height: 1;
    text-shadow: 0 1px 2px rgba(0,0,0,0.35);
  }
  .benefit-text {
    flex: 1; align-self: stretch; display: flex; align-items: center;
    padding: 4px 14px 4px 20px;
    font-size: 22px; line-height: 27px;
  }
  .benefit--blue .benefit-text { background: var(--row-blue); height: 69px; }
  .benefit--red .benefit-text { background: var(--row-red); height: 74px; }
  .benefit--magenta .benefit-text { background: var(--row-magenta); height: 75px; }
  .benefit--green .benefit-text { background: var(--row-green); height: 42px; }
  .benefit--orange .benefit-text { background: var(--row-orange); height: 52px; }
</style>
</head>
<body>
  <header class="brand-badge">
    <svg width="604" height="478" viewBox="0 0 604 478" aria-hidden="true">
      <path d="M0,0 H604 V330 Q604,360 576,372 L302,478 L28,372 Q0,360 0,330 Z" fill="var(--badge-white)"/>
      <circle cx="302" cy="160" r="92" fill="var(--brand-dot)"/>
    </svg>
    <div class="brand-name">Silverpine Orbit Works</div>
  </header>

  <h1 class="tagline">Lend us 5 minutes each morning,<br>and we will guide you toward a<br>Silverpine Orbit Works.</h1>

  <h2 class="benefits-title">Software easy enough for my grandpa to use</h2>

  <ol class="benefit-list">
    <li class="benefit benefit--blue"><span class="benefit-number">1</span><span class="benefit-text">Lets you use snail mail, email, texting, and social media to quickly market<br>to your customers at very low cost.</span></li>
    <li class="benefit benefit--red"><span class="benefit-number">2</span><span class="benefit-text">Web based which allows you to launch media campaigns from your<br>desktop, or smartphone in moments.</span></li>
    <li class="benefit benefit--magenta"><span class="benefit-number">3</span><span class="benefit-text">Quick 3 - 5 minute training videos which give you hard hitting,<br>quick action tips that will help you make your business better today.</span></li>
    <li class="benefit benefit--green"><span class="benefit-number">4</span><span class="benefit-text">Live coaching calls to help motivate you to improve your business</span></li>
    <li class="benefit benefit--orange"><span class="benefit-number">5</span><span class="benefit-text">No contracts, or start up fees. One low price of $299 per month.</span></li>
  </ol>
</body>
</html>
```